Corportate Power Point Template

We need a corporate PPT Design for our startup Big Data company.

Basically, our company will ingest, analyze and generate dynamic Dashboards with data consumed from different sources like Social Networks, Enterprise Legacy Systems such as e-Commerce, ERP, CRM and others.

Company is headquartered in Brazil, but will have a global presence.

Industry/Entity Type

It Company

```html
<!DOCTYPE html>
<html lang="en">
<head>
<meta charset="UTF-8">
<title>Project Title Here – The Open Analytics Platform</title>
<link href="https://fonts.googleapis.com/css2?family=Exo+2:wght@500;600&family=Roboto+Condensed:wght@400;500&display=swap" rel="stylesheet">
<style>
  :root {
    --orange: #f26f21;
    --orange-deep: #e2601a;
    --orange-light: #f9a23b;
    --ink: #333333;
    --text: #4a4a4a;
    --line: #e7d9cf;
    --paper: #ffffff;
    --peach: #fde6d2;
  }
  * { box-sizing: border-box; margin: 0; padding: 0; }
  html, body { width: 1200px; height: 900px; overflow: hidden; }
  body {
    font-family: "Roboto Condensed", "Arial Narrow", sans-serif;
    color: var(--ink);
    background: var(--paper);
  }
  .slide {
    position: relative;
    width: 1200px;
    height: 900px;
    overflow: hidden;
    background:
      radial-gradient(ellipse 900px 650px at 15% 35%, rgba(253, 220, 190, 0.75), rgba(255,255,255,0) 70%),
      linear-gradient(180deg, #fff6ef 0%, #ffffff 90%);
  }
  .title-bar {
    position: absolute;
    left: 0; top: 30px;
    width: 12px; height: 75px;
    background: var(--orange);
  }
  .title {
    position: absolute;
    left: 34px; top: 28px;
    font-family: "Exo 2", sans-serif;
    font-weight: 600;
    font-size: 52px;
    letter-spacing: 0.5px;
    color: var(--ink);
  }
  .title .accent { color: var(--orange); }
  .subtitle {
    position: absolute;
    left: 60px; top: 222px;
    font-size: 34px;
    font-weight: 400;
    color: var(--ink);
  }
  .pillars {
    position: absolute;
    left: 60px; top: 297px;
    display: flex;
    gap: 31px;
  }
  .pillar {
    width: 250px;
    height: 354px;
    background: var(--paper);
    border: 1.5px solid var(--orange);
    border-radius: 5px;
    text-align: center;
    padding-top: 20px;
  }
  .pillar-icon {
    display: block;
    margin: 0 auto;
    width: 180px;
    height: 120px;
  }
  .pillar-name {
    margin-top: 22px;
    font-size: 44px;
    font-weight: 400;
    color: var(--orange);
    line-height: 1;
  }
  .pillar-text {
    margin-top: 28px;
    font-size: 23px;
    line-height: 33px;
    color: var(--text);
  }
  .footer-rule {
    position: absolute;
    left: 0; right: 0; top: 818px;
    height: 1.5px;
    background: var(--line);
  }
  .presenter {
    position: absolute;
    left: 14px; top: 853px;
    font-size: 20px;
    color: #222;
  }
  .presenter .name { color: var(--orange); }
  .brand {
    position: absolute;
    right: 18px; top: 840px;
    display: flex;
    align-items: center;
    gap: 10px;
    font-family: "Exo 2", sans-serif;
    font-weight: 600;
    font-size: 38px;
    color: var(--orange);
  }
  .brand-mark {
    width: 26px; height: 26px;
    background: var(--orange);
  }
</style>
</head>
<body>
<main class="slide">
  <div class="title-bar"></div>
  <h1 class="title"><span class="accent">Project</span> Title Here</h1>

  <h2 class="subtitle">The Open Analytics Platform</h2>

  <section class="pillars">
    <article class="pillar">
      <svg class="pillar-icon" viewBox="0 0 180 120" aria-hidden="true">
        <defs>
          <linearGradient id="cloudFill" x1="0" y1="0" x2="0" y2="1">
            <stop offset="0" stop-color="#f9a23b"/>
            <stop offset="1" stop-color="#f26f21"/>
          </linearGradient>
        </defs>
        <path d="M32 100 a26 26 0 0 1 4-52 a40 40 0 0 1 74-12 a30 30 0 0 1 38 28 a20 20 0 0 1 2 36 z" fill="url(#cloudFill)"/>
        <path d="M62 62 h56 v40 h-56 z" fill="#fff"/>
        <path d="M62 62 l14 18 h28 l14 -18" fill="none" stroke="#f7c79a" stroke-width="3"/>
        <rect x="84" y="38" width="12" height="22" fill="#f26f21"/>
        <path d="M74 58 h32 l-16 16 z" fill="#f26f21"/>
      </svg>
      <h3 class="pillar-name">Collect</h3>
      <p class="pillar-text">Collect text here<br>space here Collect<br>text here space here</p>
    </article>

    <article class="pillar">
      <svg class="pillar-icon" viewBox="0 0 180 120" aria-hidden="true">
        <defs>
          <g id="inwardArrow">
            <line x1="-42" y1="-42" x2="-16" y2="-16" stroke="#f7941d" stroke-width="10"/>
            <polygon points="-7,-7 -7,-35 -35,-7" fill="#f7941d"/>
          </g>
        </defs>
        <g transform="translate(90 62)">
          <use href="#inwardArrow"/>
          <use href="#inwardArrow" transform="rotate(90)"/>
          <use href="#inwardArrow" transform="rotate(180)"/>
          <use href="#inwardArrow" transform="rotate(270)"/>
        </g>
      </svg>
      <h3 class="pillar-name">Agreggate</h3>
      <p class="pillar-text">Collect text here<br>space here Collect<br>text here space here</p>
    </article>

    <article class="pillar">
      <svg class="pillar-icon" viewBox="0 0 180 120" aria-hidden="true">
        <g fill="#f7941d">
          <rect x="52" y="12" width="5" height="96"/>
          <rect x="52" y="103" width="80" height="5"/>
          <rect x="64" y="74" width="8" height="29"/>
          <rect x="78" y="62" width="8" height="41"/>
          <rect x="92" y="66" width="8" height="37"/>
          <rect x="106" y="46" width="8" height="57"/>
        </g>
        <polyline points="60,74 80,52 96,60 124,24" fill="none" stroke="#f26f21" stroke-width="5"/>
        <path d="M118 16 h16 v16 z" fill="#f26f21"/>
        <circle cx="104" cy="84" r="15" fill="#fff" stroke="#555" stroke-width="5"/>
        <line x1="115" y1="95" x2="130" y2="110" stroke="#333" stroke-width="8" stroke-linecap="round"/>
      </svg>
      <h3 class="pillar-name">Analyze</h3>
      <p class="pillar-text">Collect text here<br>space here Collect<br>text here space here</p>
    </article>

    <article class="pillar">
      <svg class="pillar-icon" viewBox="0 0 180 120" aria-hidden="true">
        <circle cx="90" cy="62" r="46" fill="#e2651e"/>
        <path d="M60 62 q30 -30 60 0 q-30 30 -60 0 z" fill="#fff"/>
        <circle cx="90" cy="62" r="10" fill="#e2651e"/>
      </svg>
      <h3 class="pillar-name">Visualize</h3>
      <p class="pillar-text">Collect text here<br>space here Collect<br>text here space here</p>
    </article>
  </section>

  <div class="footer-rule"></div>
  <p class="presenter">Persentatator Name : <span class="name">Marina Tolledo</span></p>
  <div class="brand"><span class="brand-mark"></span>Vantix Data</div>
</main>
</body>
</html>
```